Website home page

www.quvanti.com - a website for traditional real estate and real Estate Auctions
We need a home page.
Please disregard the colors quvanti.com is designed with. Choose any colors you have in mind. Surprise us.
Home page should have the following buttons on it:
About Me
My Listings
Property Search
Buyers/Sellers
Concierge
Contact Me

Try buttons with pictures or without pictures, again, surprise us.
The page should not display property listings.
You can use property pictures - exterior and/or interior, nature or landscape pictures as an enhancement of the page. (if it will be the case)
Themes suggestions:
-modern
-hi-tech
-elegant
surprise us
Some sites that we like:
http://www.findlamberdell.com/
http://www.homesteadmarvick.com/
http://www.trivanpeak.com/
http://www.gildedhavenestates.com/
http://www.fennickpartners.com/

Target Market(s)

Home buyers and sellers

Industry/Entity Type

Real Estate

Requirements
Must have
• Home page should have the following buttons on it:
About Me
My Listings
Property Search
Buyers/Sellers
Concierge
Contact Me

```html
<!DOCTYPE html>
<html lang="en">
<head>
<meta charset="utf-8">
<title>Quvanti Real Estate</title>
<link rel="stylesheet" href="https://fonts.googleapis.com/css2?family=Arimo:wght@400;700&family=PT+Sans+Narrow:wght@700&display=swap">
<style>
:root{
  --blue-top:#3d6590;
  --blue-mid:#2c5680;
  --blue-deep:#1d3d60;
  --band:#173350;
  --gold:#e2bd2c;
  --gold-soft:#f2de72;
  --text:#d5dde6;
  --frame:#ffffff;
  --footer:#1d1d1d;
  --footer-text:#9a9a9a;
  --footer-head:#a8a8a8;
}
*{margin:0;padding:0;box-sizing:border-box}
html,body{width:1038px;height:1200px;overflow:hidden;background:var(--footer)}
body{font-family:"Arimo",Helvetica,Arial,sans-serif;position:relative}
.page{position:relative;width:1038px;height:1200px;overflow:hidden}

/* header */
.hero{position:absolute;left:0;top:0;width:1038px;height:424px;
  background:radial-gradient(ellipse at 50% 30%,#4b75a0 0%,var(--blue-top) 35%,var(--blue-mid) 70%,#244a72 100%)}
.brand{position:absolute;left:111px;top:22px;display:flex;align-items:center;gap:8px;
  font-family:"Arimo",sans-serif;font-weight:700;font-size:42px;color:var(--gold);letter-spacing:-1px}
.brand-dot{width:14px;height:14px;border-radius:50%;background:var(--gold)}
.nav{position:absolute;top:32px;left:0;width:1038px;height:22px;list-style:none;
  font-family:"PT Sans Narrow",sans-serif;font-weight:700;font-size:15px}
.nav li{position:absolute;top:3px;color:var(--gold);white-space:nowrap}
.nav li.active{top:0;left:365px;width:85px;height:22px;padding-top:3px;text-align:center;color:#fff;
  border:1px solid rgba(255,255,255,.35);border-bottom:none;border-radius:4px 4px 0 0;
  background:linear-gradient(rgba(255,255,255,.12),rgba(255,255,255,0))}

.slide{position:absolute;background:var(--frame);padding:5px;box-shadow:0 3px 10px rgba(0,0,0,.35)}
.slide .photo{width:100%;height:100%}
.slide-side{width:209px;height:166px;top:181px}
.slide-left{left:112px}
.slide-right{left:717px}
.slide-main{left:329px;top:117px;width:379px;height:256px}
.reflect{position:absolute;background:linear-gradient(rgba(255,255,255,.09),rgba(255,255,255,0))}
.photo-a{background:linear-gradient(#6f9fd4 0%,#9dbde0 45%,#e8e6df 55%,#5f8a3a 80%,#4a7030 100%)}
.photo-b{background:linear-gradient(#6fa4e0 0%,#a9c8e8 35%,#efe3c0 50%,#d9c89c 75%,#3d3f44 90%,#2d2f33 100%)}
.photo-c{background:linear-gradient(#4b8ee0 0%,#8fbbee 40%,#cdb7a0 55%,#b59b84 72%,#6c9a3d 85%,#5a8632 100%)}
.dots{position:absolute;top:396px;left:443px;display:flex;gap:30px}
.dots span{width:10px;height:10px;border-radius:50%;background:radial-gradient(circle at 40% 35%,#4c6f94,#0d1f33)}

/* content */
.divider{position:absolute;left:0;top:424px;width:1038px;height:8px;background:var(--band);border-bottom:1px solid #2f5378}
.content{position:absolute;left:0;top:432px;width:1038px;height:534px;
  background:linear-gradient(var(--blue-mid),var(--blue-deep))}
.panel{position:absolute;left:117px;top:0;width:811px;height:534px;
  background:linear-gradient(rgba(255,255,255,.05),rgba(255,255,255,.02));
  box-shadow:0 0 14px rgba(0,0,0,.2)}
.welcome{position:absolute;left:0;top:30px;width:1038px;text-align:center;
  font-size:26px;font-weight:700;color:var(--gold);letter-spacing:-1px}
.lead{position:absolute;left:152px;top:80px;font-size:14px;color:var(--gold-soft)}
.intro{position:absolute;left:152px;width:733px;font-size:12px;line-height:15.6px;color:var(--text);text-align:justify}
.intro-1{top:124px}
.intro-2{top:187px}
.read-more{position:absolute;right:153px;top:228px;font-size:10.5px;color:var(--text);text-decoration:underline;display:flex;align-items:center;gap:6px}
.rule{position:absolute;left:152px;top:253px;width:733px;height:1px;background:rgba(255,255,255,.1)}
.featured-title{position:absolute;left:152px;top:272px;font-size:22px;font-weight:700;color:var(--gold);letter-spacing:-1px}
.featured{position:absolute;left:154px;top:313px;display:grid;grid-template-columns:repeat(5,118px);column-gap:35px;row-gap:26px}
.card-name{height:15px;font-size:12px;font-weight:700;color:var(--gold-soft);letter-spacing:-.5px;white-space:nowrap;display:flex;align-items:center;gap:6px}
.card-name::before{content:"";width:4px;height:4px;background:var(--gold)}
.card-photo{width:118px;height:74px;background:var(--frame);padding:4px}
.card-photo div{width:100%;height:100%}
.ext-1{background:linear-gradient(#b7cbe0 0%,#d6dde2 40%,#8e8f86 60%,#5d7a3c 100%)}
.ext-2{background:linear-gradient(#2f5a2a 0%,#5d8b3c 40%,#e5e0cf 55%,#4e7d33 100%)}
.ext-3{background:linear-gradient(#6fa8e6 0%,#bcd6f0 40%,#e9e4d8 60%,#4d8a33 100%)}
.ext-4{background:linear-gradient(#a9c7ea 0%,#e8ebef 45%,#f0f0f0 65%,#6b8a4a 100%)}
.int-1{background:linear-gradient(90deg,#c9b199,#8a6b55 50%,#d2bda6)}
.int-2{background:linear-gradient(#d7cfc0 0%,#6a5a4a 55%,#3f3934 100%)}
.int-3{background:linear-gradient(90deg,#d8d8d6,#f4f4f2 50%,#6d6a66)}
.int-4{background:linear-gradient(#d8c25a 0%,#c3a84b 45%,#a07440 75%,#6b4a2e 100%)}

/* footer */
.footer{position:absolute;left:0;top:966px;width:1038px;height:234px;
  background:linear-gradient(#2a2a2a,var(--footer) 40%,#151515);color:var(--footer-text);font-size:10px}
.foot-head{position:absolute;top:34px;font-family:"PT Sans Narrow",sans-serif;font-weight:700;font-size:15px;color:var(--footer-head)}
.foot-links{position:absolute;top:56px;list-style:none}
.foot-links li{height:20.5px;display:flex;align-items:center;gap:8px;white-space:nowrap}
.foot-links li::before{content:"";width:0;height:0;border-left:4px solid #777;border-top:3px solid transparent;border-bottom:3px solid transparent}
.contact{position:absolute;left:720px;top:56px;list-style:none}
.contact li{display:flex;align-items:center;gap:10px;height:20.5px;white-space:nowrap}
.contact li.address{height:auto;align-items:flex-start;margin-top:4px;line-height:15px}
.contact svg{width:15px;height:15px;flex:none;fill:#8a8a8a}
.foot-rule{position:absolute;left:108px;top:168px;width:831px;height:1px;background:#333}
.copyright{position:absolute;left:0;top:185px;width:1038px;text-align:center;font-size:11px}
</style>
</head>
<body>
<div class="page">
  <header class="hero">
    <div class="brand"><span class="brand-dot"></span>Quvanti</div>
    <ul class="nav">
      <li class="active">About Me</li>
      <li style="left:471px">My Listings</li>
      <li style="left:560px">Property Search</li>
      <li style="left:676px">Buyers / Sellers</li>
      <li style="left:789px">Concierge</li>
      <li style="left:868px">Contac Me</li>
    </ul>

    <div class="reflect" style="left:112px;top:349px;width:209px;height:40px"></div>
    <div class="reflect" style="left:329px;top:375px;width:379px;height:40px"></div>
    <div class="reflect" style="left:717px;top:349px;width:209px;height:40px"></div>

    <div class="slide slide-side slide-left"><div class="photo photo-a" role="img" aria-label="Two-storey white suburban house with green lawn"></div></div>
    <div class="slide slide-main"><div class="photo photo-b" role="img" aria-label="Row of cream townhouses under a blue sky"></div></div>
    <div class="slide slide-side slide-right"><div class="photo photo-c" role="img" aria-label="Stucco family home with a turret and front lawn"></div></div>
    <div class="dots"><span></span><span></span><span></span><span></span></div>
  </header>

  <div class="divider"></div>

  <main class="content">
    <div class="panel"></div>
    <h1 class="welcome">Welcome to Quvanti Real Esteate</h1>
    <p class="lead">Elit ipsum, blandit sed pellentesque</p>
    <p class="intro intro-1">Nunc elit ipsum, blandit sed pellentesque nec, condimentum non sem. Pellentesque eleifend auctor eros ut mollis. Donec eget arcu nulla. Duis orci neque, vehicula sodales laoreet faucibus, venenatis a erat. Curabitur ipsum nisi, porta pharetra convallis et, ullamcorper ut mi. Integer eu nunc dui, ut fermentum nulla. Maecenas a nisi eget massa suscipit dictum quis ultrices velit. Sed ac elementum mauris.</p>
    <p class="intro intro-2">Donec tincidunt arcu sit amet purus gravida condimentum. Quisque posuere tellentesque quis nisi sit amet purus tempus bibendum vel eget leo.urpis eget risus cursus quis pulvinar tellus tristique.</p>
    <a class="read-more"><svg width="9" height="7" viewBox="0 0 9 7"><path d="M0 3.5h8M5 0.5l3 3-3 3" stroke="#c8d2de" fill="none"/></svg>read more</a>
    <div class="rule"></div>
    <h2 class="featured-title">Featured Property</h2>

    <div class="featured">
      <div><p class="card-name">In facilisis nulla</p><div class="card-photo"><div class="ext-1" role="img" aria-label="Grey farmhouse with wraparound porch"></div></div></div>
      <div><p class="card-name">Maecenas eleme est</p><div class="card-photo"><div class="ext-2" role="img" aria-label="Colonial house among trees"></div></div></div>
      <div><p class="card-name">Interdum aliquet odio</p><div class="card-photo"><div class="ext-3" role="img" aria-label="Two-storey house with porch and hedges"></div></div></div>
      <div><p class="card-name">Lorem sed nisi</p><div class="card-photo"><div class="ext-4" role="img" aria-label="Large white family home"></div></div></div>
      <div><p class="card-name">Praesent hendrerit</p><div class="card-photo"><div class="ext-4" role="img" aria-label="Large white family home"></div></div></div>

      <div><p class="card-name">In facilisis nulla</p><div class="card-photo"><div class="int-1" role="img" aria-label="Entry hall with staircase"></div></div></div>
      <div><p class="card-name">Maecenas eleme est</p><div class="card-photo"><div class="int-2" role="img" aria-label="Dining room with chandelier"></div></div></div>
      <div><p class="card-name">Interdum aliquet odio</p><div class="card-photo"><div class="int-3" role="img" aria-label="Modern white living room"></div></div></div>
      <div><p class="card-name">Lorem sed nisi</p><div class="card-photo"><div class="int-4" role="img" aria-label="Warm yellow bedroom"></div></div></div>
      <div><p class="card-name">Praesent hendrerit</p><div class="card-photo"><div class="int-4" role="img" aria-label="Warm yellow bedroom"></div></div></div>
    </div>
  </main>

  <footer class="footer">
    <h3 class="foot-head" style="left:126px">Navigation</h3>
    <ul class="foot-links" style="left:128px"><li>About Me</li><li>My Listings</li><li>Property Search</li></ul>
    <ul class="foot-links" style="left:227px"><li>Buyers/Sellers</li><li>Concierge</li><li>Contact Me</li></ul>

    <h3 class="foot-head" style="left:375px">How to...</h3>
    <ul class="foot-links" style="left:376px"><li>How to Buy</li><li>How to Sell</li><li>Services to Help You Sell</li></ul>
    <ul class="foot-links" style="left:516px"><li>For Agents</li><li>Terms &amp; Conditions</li><li>Privacy Policy</li></ul>

    <h3 class="foot-head" style="left:711px;top:32px">Contac Us</h3>
    <ul class="contact">
      <li><svg viewBox="0 0 16 16"><path d="M1 5c0-2 3-3 7-3s7 1 7 3v1h-4V4.5H5V6H1zM3 7h10l1 7H2z"/></svg>office: (555) 204-7731</li>
      <li><svg viewBox="0 0 16 16"><path d="M4 1h8v4H4zM1 6h14v6h-3v3H4v-3H1zM5 10v4h6v-4z"/></svg>fax: (555) 318-6420</li>
      <li><svg viewBox="0 0 16 16"><path d="M1 3h14v10H1zM2 4l6 5 6-5v-.2H2z" fill-rule="evenodd"/></svg>email: support@quvanti.com</li>
      <li class="address"><svg viewBox="0 0 16 16"><path d="M7 0h2v2h5l2 2-2 2H9v2H3L1 10l2 2h4v4h2v-4H7z"/></svg><span>48 Larkmoor Lane, Suite 210<br>Wendle Bay, CA 90000</span></li>
    </ul>

    <div class="foot-rule"></div>
    <p class="copyright">© 2012 Quvanti, All rigths reserved</p>
  </footer>
</div>
</body>
</html>
```